Road Construction Company needs business cards

We would like a new business card designed for our business.

We're a road construction company based in Qld, Australia.

Can the business card please have the following information on it.

Name: Brent Malvoy
Position: General Manager
Phone: 0471 592 304
Email: Brent.malvoy@quendix.com.au
Address: 87 Harrowgate Ave, Pindarra, QLD, 4000
Website: www.quendix.com.au

Visually we'd like the card to be professional and simple.

Attached is our logo.

Our website is www.quendix.com.au

Target Market(s)

Men aged 25-60

Contact Information for Business Card

As listed in project description

Font styles to use
Serif

Requirements
Must have
• Large logo on back of card

```html
<!DOCTYPE html>
<html lang="en">
<head>
<meta charset="utf-8">
<title>Quendix Road Construction – Business Card</title>
<link rel="stylesheet" href="https://fonts.googleapis.com/css2?family=Tinos:wght@400;700&display=swap">
<style>
  :root {
    --navy: #0353a4;
    --sky: #35a5d8;
    --paper: #ffffff;
    --backdrop: #e6e6e6;
  }
  * { margin: 0; padding: 0; box-sizing: border-box; }
  html, body { width: 1200px; height: 1200px; overflow: hidden; background: var(--backdrop); }
  body { position: relative; font-family: "Tinos", "Times New Roman", serif; }

  .card { position: absolute; left: 265px; width: 690px; height: 394px; overflow: hidden; }
  .card--front { top: 173px; background: var(--paper); }
  .card--back { top: 644px; background: var(--navy); }

  .wordmark { position: absolute; font-weight: 700; line-height: 1; white-space: nowrap; }
  .wordmark__name { display: block; letter-spacing: 2px; }
  .wordmark__tag { display: block; font-weight: 700; text-transform: uppercase; color: var(--sky); }

  .card--front .wordmark { left: 50px; top: 46px; color: var(--navy); }
  .card--front .wordmark__name { font-size: 56px; }
  .card--front .wordmark__tag { font-size: 11px; letter-spacing: 7.6px; margin-top: 3px; }

  .card--back .wordmark { left: 0; right: 0; top: 138px; text-align: center; color: #fff; }
  .card--back .wordmark__name { font-size: 88px; letter-spacing: 5px; }
  .card--back .wordmark__tag { font-size: 18px; letter-spacing: 15px; margin-top: 6px; padding-left: 15px; }

  .person__name { position: absolute; left: 49px; top: 152px; font-size: 31px; font-weight: 400; color: var(--navy); line-height: 1; }
  .person__role { position: absolute; left: 51px; top: 185px; font-size: 9px; letter-spacing: 1px; color: var(--sky); }
  .person__rule { position: absolute; left: 162px; top: 189.5px; width: 478px; height: 1px; background: var(--sky); }

  .contacts { list-style: none; }
  .contact { position: absolute; left: 49px; display: flex; align-items: center; gap: 15px; font-size: 18.5px; color: var(--sky); }
  .contact__icon { width: 27px; height: 27px; flex: none; }
  .contact--phone { top: 211px; }
  .contact--mail { top: 252px; }
  .contact--web { top: 294px; }

  .address { position: absolute; right: 50px; top: 214px; text-align: right; font-size: 18.5px; line-height: 21px; color: var(--sky); font-style: normal; }

  .footer-band { position: absolute; left: 0; right: 0; bottom: 0; height: 52px; background: linear-gradient(90deg, var(--navy) 0%, var(--navy) 55%, var(--sky) 100%); }
</style>
</head>
<body>

<section class="card card--front">
  <div class="wordmark">
    <span class="wordmark__name">QUENDIX</span>
    <span class="wordmark__tag">Road Construction</span>
  </div>

  <h1 class="person__name">Brent Malvoy</h1>
  <p class="person__role">GENERAL MANAGER</p>
  <div class="person__rule"></div>

  <ul class="contacts">
    <li class="contact contact--phone">
      <svg class="contact__icon" viewBox="0 0 28 28" aria-hidden="true">
        <circle cx="14" cy="14" r="14" fill="var(--navy)"/>
        <path d="M9.5 7.5c.6-.5 1.4-.4 1.8.2l1.4 2.1c.3.5.2 1.2-.2 1.6l-.9.8c.6 1.6 1.8 2.9 3.4 3.6l.8-.9c.4-.4 1.1-.5 1.6-.2l2.1 1.3c.6.4.7 1.2.2 1.8l-.9 1c-.7.8-1.9 1-2.9.6-3.5-1.4-6.3-4.2-7.6-7.7-.4-1-.2-2.1.6-2.8z" fill="#fff"/>
      </svg>
      <span>0471 592 304</span>
    </li>
    <li class="contact contact--mail">
      <svg class="contact__icon" viewBox="0 0 28 28" aria-hidden="true">
        <circle cx="14" cy="14" r="14" fill="var(--navy)"/>
        <rect x="7.5" y="9.5" width="13" height="9" fill="none" stroke="#fff" stroke-width="1.4"/>
        <path d="M7.5 9.5 L14 15 L20.5 9.5 M7.5 18.5 L12 14 M20.5 18.5 L16 14" fill="none" stroke="#fff" stroke-width="1.2"/>
      </svg>
      <span>Brent.malvoy@quendix.com.au</span>
    </li>
    <li class="contact contact--web">
      <svg class="contact__icon" viewBox="0 0 28 28" aria-hidden="true">
        <circle cx="14" cy="14" r="14" fill="var(--navy)"/>
        <circle cx="14" cy="14" r="7.5" fill="none" stroke="#fff" stroke-width="1.4"/>
        <ellipse cx="14" cy="14" rx="3.2" ry="7.5" fill="none" stroke="#fff" stroke-width="1.1"/>
        <path d="M6.5 14 H21.5" stroke="#fff" stroke-width="1.1"/>
      </svg>
      <span>www.quendix.com.au</span>
    </li>
  </ul>

  <address class="address">87 Harrowgate Ave,<br>Pindarra, QLD, 4000</address>

  <div class="footer-band" role="img" aria-label="Decorative navy and sky blue wave band along the card's lower edge"></div>
</section>

<section class="card card--back">
  <div class="wordmark">
    <span class="wordmark__name">QUENDIX</span>
    <span class="wordmark__tag">Road Construction</span>
  </div>
</section>

</body>
</html>
```